BRV Coffee bag (front and back)

We use black matte bags and have front and back labels. We have a logo but need an attractive and inviting label. The labels will be used for our entire line of coffees. We sell most of our coffee to foodservice establishments (Restaurants, Hotels, Bakeries, Bodegas) and we would like to have these establishments display our bags of coffee to sell retail.
The logo can be used as a whole or using any one of the three components (Logo, image, tag).

Target Market(s)

People who buy the coffee they brew at home from the local shop they get their morning latte.. We are a local coffee company, but we do not sell locally roasted coffee!

Industry/Entity Type

Food

Font styles to use
Other font styles liked:
• something that looks good with our trademarked BRV

Colors

Designer to choose colors to be used in the design.

Requirements
Must have
• Respect Trademarked logo
Nice to have
• It would be nice to have a design that can be used with other mediums (airpot wraps, java jackets, )
Should not have
• Real People

```html
<!DOCTYPE html>
<html lang="en">
<head>
<meta charset="utf-8">
<title>BRV Coffee Label</title>
<link rel="stylesheet" href="https://fonts.googleapis.com/css2?family=Barlow:wght@300;400;600;700&display=swap">
<style>
  :root {
    --page: #ececec;
    --label-dark: #231f20;
    --brand-red: #ed1c24;
    --white: #ffffff;
    --frame-grey: #8a8a8a;
    --illus-grey: #5a5556;
    --illus-berry: #8a3a1c;
  }
  * { margin: 0; padding: 0; box-sizing: border-box; }
  html, body { width: 1200px; height: 970px; overflow: hidden; background: var(--page); }
  body { position: relative; font-family: "Barlow", sans-serif; }

  .label {
    position: absolute; left: 303px; top: 35px;
    width: 594px; height: 900px;
    background: var(--label-dark);
    border-radius: 44px; overflow: hidden;
  }
  .botanical-art {
    position: absolute; left: 0; top: 0; width: 594px; height: 300px;
    background: linear-gradient(180deg, var(--illus-grey) 0%, #4a3a34 35%, var(--illus-berry) 60%, var(--label-dark) 100%);
    opacity: .85;
  }
  .ribbon {
    position: absolute; left: 230px; top: 0; width: 131px; height: 142px;
    background: var(--brand-red);
  }
  .emblem { position: absolute; left: 194px; top: 124px; }

  .brand-name {
    position: absolute; left: 0; width: 594px; top: 345px;
    text-align: center; color: var(--white);
    font-weight: 300; font-size: 168px; line-height: 1; letter-spacing: 6px;
  }
  .brand-tagline {
    position: absolute; left: 0; width: 594px; top: 505px;
    text-align: center; color: var(--white);
    font-weight: 400; font-size: 16px; letter-spacing: 6.5px;
  }

  .info-box {
    position: absolute; left: 80px; top: 570px; width: 432px; height: 229px;
    border: 4px solid var(--frame-grey); border-radius: 14px;
    background: var(--white); overflow: hidden;
  }
  .product-title {
    height: 129px; padding: 14px 0 0 26px;
    font-weight: 700; font-size: 52px; line-height: 50px; color: var(--label-dark);
    border-bottom: 3px solid var(--frame-grey);
  }
  .product-details { display: flex; height: 93px; }
  .roast-type {
    width: 190px; background: var(--label-dark); color: var(--white);
    padding: 12px 0 0 24px; font-weight: 600; font-size: 27px; line-height: 31px;
  }
  .tasting-notes {
    flex: 1; padding: 12px 0 0 22px; color: var(--label-dark);
    font-weight: 400; font-size: 20px; line-height: 23px; letter-spacing: .5px;
  }
  .quality-seal { position: absolute; left: 438px; top: 528px; }

  .weight-band {
    position: absolute; left: 0; top: 824px; width: 594px; height: 76px;
    background: var(--brand-red); color: var(--white);
    text-align: center; font-weight: 600; font-size: 25px; line-height: 68px;
  }
</style>
</head>
<body>
  <div class="label">
    <div class="botanical-art" role="img" aria-label="Illustrated coffee branches with grey leaves, white blossoms and ripe red-brown coffee cherries"></div>
    <div class="ribbon"></div>
    <svg class="emblem" width="206" height="206" viewBox="0 0 206 206" aria-hidden="true">
      <circle cx="103" cy="103" r="96" fill="var(--label-dark)" stroke="var(--brand-red)" stroke-width="12"/>
    </svg>

    <div class="brand-name">BRV</div>
    <div class="brand-tagline">Bravo Roasting Ventures</div>

    <div class="info-box">
      <div class="product-title">GOLD CREMA<br>ESPRESSO</div>
      <div class="product-details">
        <div class="roast-type">ESPRESSO<br>ROAST</div>
        <div class="tasting-notes">Notes:<br>A rich, classic<br>espresso blend</div>
      </div>
    </div>
    <svg class="quality-seal" width="120" height="120" viewBox="0 0 120 120" aria-hidden="true">
      <circle cx="60" cy="60" r="55" fill="var(--white)" stroke="var(--brand-red)" stroke-width="3"/>
    </svg>

    <div class="weight-band">2 Lb. Whole Bean Coffee</div>
  </div>
</body>
</html>
```